Political Association Member Newsletter

We require a professional newsletter designed that will be sent both by mail and by email (and can be posted online) to the members in our client organization. I will develop and curate the content to send to the designer but we need help with a good design.

We have two key colours: red and blue (usually on white background). The pantones are:
blue = 301C
red = 032C

The logo I have from the client is attached as well as a recent piece with contact information and social media channels noted.

The client also provided a campaign logo "Raise the Bar for 2019" that will accompany copy for membership and donation which will follow.

Two preliminary content pieces are also included here: a flyer for a bbq and the "Regional Forum Digest" article.

Political

Sans Serif

• Space for pictures - uploaded below.

```html
<!DOCTYPE html>
<html lang="en">
<head>
<meta charset="utf-8">
<title>Riverbend Centre Newsletter – First Edition</title>
<link rel="stylesheet" href="https://fonts.googleapis.com/css2?family=Fira+Sans+Condensed:wght@400;600;700&family=Fira+Sans+Extra+Condensed:ital,wght@0,600;0,700;1,400&family=Lato:wght@300;400;700;900&family=Rye&display=swap">
<style>
  :root{
    --backdrop:#fde8c8;
    --paper:#ffffff;
    --blue:#1a4b8c;
    --blue-deep:#1d2f6f;
    --navy:#24285f;
    --red:#e8333d;
    --wine:#6d1326;
    --wine-deep:#3d0711;
    --gold:#f8c33b;
    --ink:#1b1b1b;
    --caption-bg:#e7e7e7;
    --caption-ink:#3a3a3a;
  }
  *{margin:0;padding:0;box-sizing:border-box}
  html,body{width:900px;height:1200px;overflow:hidden;background:var(--backdrop)}
  body{position:relative;font-family:"Fira Sans Condensed",sans-serif;color:var(--ink)}
  .sheet{position:absolute;left:206px;top:36px;width:488px;height:1110px;background:var(--paper);box-shadow:3px 4px 8px rgba(0,0,0,.25);overflow:hidden}
  .abs{position:absolute}

  /* masthead */
  .brand{left:18px;top:32px;display:flex;align-items:center;gap:10px}
  .brand-mark{width:50px;height:50px;border-radius:50%;background:var(--blue-deep)}
  .brand-name{font-weight:700;font-size:15px;line-height:17px;color:var(--blue-deep);letter-spacing:-.2px}
  .title{right:18px;top:38px;text-align:right;color:var(--navy)}
  .title-main{font-family:"Lato",sans-serif;font-size:27px;line-height:28px;letter-spacing:.3px}
  .title-main b{font-weight:900}
  .title-main span{font-weight:400}
  .title-sub{font-weight:700;font-size:10.5px;letter-spacing:.2px;margin-top:2px}
  .social{right:24px;top:89px;display:flex;align-items:center;gap:6px;font-size:7px;color:var(--ink)}
  .social i{display:inline-block;width:16px;height:16px;background:var(--blue)}
  .social .gap{width:12px}
  .edition-bar{left:0;top:117px;width:488px;height:16px;background:var(--blue);color:#fff;font-weight:700;font-size:11px;line-height:16px}
  .edition-bar .red{position:absolute;left:66px;top:0;width:62px;height:16px;background:var(--red);border-left:3px solid #fff;border-right:3px solid #fff}
  .edition-bar .label{position:absolute;left:141px}
  .edition-bar .date{position:absolute;right:14px}

  .section-title{font-family:"Lato",sans-serif;font-weight:900;font-size:21px;color:#fff;letter-spacing:.2px;white-space:nowrap}
  .more{font-family:"Lato",sans-serif;font-size:11px;color:#fff}

  /* member */
  .member{left:0;top:150px;width:488px;height:218px;background:radial-gradient(circle at 70% 60%,#2b5aa0 0%,var(--blue-deep) 80%)}
  .member .section-title{position:absolute;left:23px;top:16px}
  .portrait-frame{position:absolute;left:23px;top:53px;width:138px;height:138px;background:#fff;padding:6px}
  .portrait{width:100%;height:100%;background:linear-gradient(180deg,#d9d9d9 0%,#c4b6ac 55%,#2a2e38 100%)}
  .member-name{position:absolute;left:186px;top:58px;font-size:20px;font-weight:600;color:#fff}
  .member-text{position:absolute;left:186px;top:87px;width:276px;font-family:"Fira Sans Extra Condensed",sans-serif;font-size:11px;line-height:14.3px;font-weight:600;color:#fff}
  .member .more{position:absolute;right:37px;top:176px}

  /* event */
  .event-tag{left:0;top:373px;width:172px;height:91px;background:var(--blue);padding:17px 0 0 23px}
  .event-tag .section-title{line-height:26px}
  .event-tag svg{position:absolute;left:141px;top:33px}
  .event-art{left:290px;top:380px;width:60px;height:80px;background:linear-gradient(180deg,rgba(80,140,220,.18),rgba(80,140,220,.06))}
  .event-name{left:172px;top:390px;width:316px;text-align:center;font-family:"Rye",serif;font-variant:small-caps;font-size:19px;line-height:24px;color:var(--blue-deep);white-space:nowrap}
  .event-more{left:0;top:448px;width:451px;text-align:right;color:var(--blue-deep)}

  /* renew */
  .renew{left:0;top:469px;width:488px;height:218px;background:radial-gradient(ellipse at 50% 30%,var(--wine) 0%,var(--wine-deep) 100%);color:#fff}
  .renew .section-title{position:absolute;left:0;top:15px;width:100%;text-align:center}
  .renew ul{position:absolute;left:62px;top:53px;list-style:none;font-weight:700;font-size:14.5px;line-height:20px;white-space:nowrap}
  .renew li::before{content:"";display:inline-block;width:7px;height:7px;border-radius:50%;background:#fff;margin-right:9px;vertical-align:2px}
  .plan{position:absolute;top:106px;width:132px;height:56px;background:var(--gold);color:var(--ink);display:flex;align-items:center;justify-content:center;font-family:"Lato",sans-serif}
  .plan .price{font-weight:900;font-size:31px}
  .plan .slash{font-weight:300;font-size:44px;margin:0 2px 0 0;transform:skewX(-8deg)}
  .plan .term{font-family:"Fira Sans Condensed",sans-serif;font-weight:700;font-size:12px;line-height:14px;text-align:left;padding-top:6px}
  .plan .term b{display:block;font-size:14px}
  .renew-contact{position:absolute;left:0;top:177px;width:100%;text-align:center;font-family:"Lato",sans-serif;font-size:11px;line-height:13px;color:#f1dcdc}

  /* photos */
  .photos-head{left:0;top:693px;width:488px;height:39px;background:var(--blue);padding:8px 0 0 23px}
  .photo{position:absolute}
  .photo-stage{left:26px;top:743px;width:220px;height:165px;background:linear-gradient(180deg,#0d1430 0%,#1e3a8a 55%,#151a2c 100%)}
  .photo-group{left:26px;top:918px;width:220px;height:100px;background:linear-gradient(180deg,#7d7666 0%,#4a4036 100%)}
  .photo-hall{left:256px;top:743px;width:206px;height:275px;background:linear-gradient(180deg,#223c8c 0%,#3b3f55 40%,#1d1d22 100%)}
  .captions{left:26px;top:1028px;width:436px;height:68px;background:var(--caption-bg);padding:6px 10px;font-family:"Fira Sans Extra Condensed",sans-serif;font-style:italic;font-weight:400;font-size:12.6px;line-height:17px;color:var(--caption-ink);white-space:nowrap;overflow:hidden}
</style>
</head>
<body>
<main class="sheet">
  <header>
    <div class="abs brand">
      <span class="brand-mark"></span>
      <p class="brand-name">Civic Reform Party,<br>Riverbend Centre</p>
    </div>
    <div class="abs title">
      <p class="title-main"><b>NEWS</b><span>LETTER</span></p>
      <p class="title-sub">MONTHLY EDITIONS</p>
    </div>
    <div class="abs social">
      <i></i><span>Riverbend Centre Reform Association</span>
      <span class="gap"></span>
      <i></i><span>@RiverbendCRP</span>
    </div>
    <div class="abs edition-bar">
      <span class="red"></span>
      <span class="label">FIRST EDITION</span>
      <span class="date">15th July 2016</span>
    </div>
  </header>

  <section class="abs member">
    <h2 class="section-title">MEMBER OF THIS MONTH</h2>
    <div class="portrait-frame"><div class="portrait" role="img" aria-label="Portrait photo of the featured member"></div></div>
    <h3 class="member-name">Daniel Marchetti</h3>
    <p class="member-text">It’s my pleasure to introduce myself as the newest member of National Council from Prairie. &nbsp;I will join Helen Brandt from Stonebridge representing the views of members from across the province. &nbsp;I’ve met many of you over the years, in particular during my three years as EDA President in Riverbend Centre, and I’m looking forward to working for you again.</p>
    <p class="more">Find more below</p>
  </section>

  <section>
    <div class="abs event-tag">
      <h2 class="section-title">MONTH’S<br>EVENT</h2>
      <svg width="14" height="24" viewBox="0 0 14 24"><path d="M3 3 L11 12 L3 21" fill="none" stroke="#fff" stroke-width="3"/></svg>
    </div>
    <div class="abs event-art" role="img" aria-label="Faint barbecue grill illustration"></div>
    <p class="abs event-name">Northern Prairie<br>Members Summer BBQ</p>
    <p class="abs more event-more">Find more below</p>
  </section>

  <section class="abs renew">
    <h2 class="section-title">RENEW YOUR MEMBERSHIP TODAY</h2>
    <ul>
      <li>Be part of deciding who the next leader of our party will be</li>
      <li>Receive information about upcoming events &amp; activities</li>
    </ul>
    <div class="plan" style="left:30px"><span class="price">$15</span><span class="slash">/</span><span class="term"><b>1</b>Year</span></div>
    <div class="plan" style="left:178px"><span class="price">$25</span><span class="slash">/</span><span class="term"><b>2</b>Years</span></div>
    <div class="plan" style="left:326px"><span class="price">$50</span><span class="slash">/</span><span class="term"><b>5</b>Years</span></div>
    <p class="renew-contact">to renew your membership today visit civicreform.ca<br>or call us at 555-014-2780</p>
  </section>

  <section>
    <div class="abs photos-head"><h2 class="section-title">THIS MONTH’S PHOTOS</h2></div>
    <div class="photo photo-stage" role="img" aria-label="Convention hall with speaker on stage and large screens"></div>
    <div class="photo photo-group" role="img" aria-label="Three members posing together at the convention"></div>
    <div class="photo photo-hall" role="img" aria-label="Members seated at a long table in the convention hall"></div>
    <div class="abs captions">
      <p>(Image Top Left): Lorem ipsum dolor sit amet, consectetuer adipiscing elit, sed diam</p>
      <p>(Image Bottom Left): Nibh euismod tincidunt ut laoreet dolore magna aliquam erat</p>
      <p>(Image Right): Ut wisi enim ad minim veniam, quis nostrud exerci tation ullamcorper</p>
    </div>
  </section>
</main>
</body>
</html>
```